Fitness Packaging

The attached box will be a new fitness product (see pictures). I need a graphic design for this box using the colors of black and yellow or black, yellow and silver. Please do not put any words, text, pictures of people, or any fitness equipment in the design. I just need your idea of an active, fitness, fun graphic design using the colors I mentioned. Please feel free to ask me any questions. Also, please see my "target market" section if it helps.

Measurements:

5.25" across

6" long or length

1 15/16" depth or deep

Cut out:

1 3/16" from top

3 5/8" from left

2 3/16" from bottom

Entire width of depth of right side is cut out

Cut out is 2 11/16" in length

Cut out is 1 5/8" cross missing from the front of the box

Cut out is 1 15/16" wide missing from the side

Hanging tag is 1 3/8" long

5 3/16 wide
Updates

Project Deadline Extended
Reason: I didn't get many design submissions.

Target Market(s)

Men and women (but maybe mostly men) from athletes to a Pearson who simply works out. Their age ranges will be between 19 years old to 40 years old. This product would have about the same target market (women can use also) as the Brisk Lift-Bar https://briskgearhub.example/item/Liftbar

Industry/Entity Type

Fitness Equipment

Colors
fbed22

Requirements
Must have
• Black and yellow or black, yellow, and silver
Should not have
• Please do not put any words, text, pictures of people, or any fitness equipment in the design

```html
<!DOCTYPE html>
<html lang="en">
<head>
<meta charset="utf-8">
<title>Fitness Packaging Dieline</title>
<style>
  :root {
    --paper: #ffffff;
    --ink: #000000;
    --accent-yellow: #fff200;
    --fold-line: #c9c9cc;
  }
  html, body {
    margin: 0;
    padding: 0;
    width: 1200px;
    height: 866px;
    overflow: hidden;
    background: var(--paper);
  }
  .dieline {
    display: block;
    width: 1200px;
    height: 866px;
  }
  .panel-black { fill: var(--ink); }
  .band-yellow { fill: var(--accent-yellow); }
  .window-cutout, .hang-slot { fill: var(--paper); }
  .fold { stroke: var(--fold-line); stroke-width: 0.8; fill: none; }
</style>
</head>
<body>
<svg class="dieline" viewBox="0 0 1300 938" preserveAspectRatio="none" role="img" aria-label="Flat box dieline with black top flaps, a yellow band and silver gradient side panels">
  <defs>
    <linearGradient id="silver-back" gradientUnits="userSpaceOnUse" x1="104" y1="0" x2="481" y2="0">
      <stop offset="0" stop-color="#e2dfdc"/>
      <stop offset="0.5" stop-color="#b0adb1"/>
      <stop offset="0.78" stop-color="#8a888e"/>
      <stop offset="1" stop-color="#a6a3a8"/>
    </linearGradient>
    <linearGradient id="silver-side-left" gradientUnits="userSpaceOnUse" x1="481" y1="0" x2="621" y2="0">
      <stop offset="0" stop-color="#b0aeb4"/>
      <stop offset="1" stop-color="#d9d8dc"/>
    </linearGradient>
    <linearGradient id="silver-front" gradientUnits="userSpaceOnUse" x1="622" y1="0" x2="999" y2="0">
      <stop offset="0" stop-color="#dedee2"/>
      <stop offset="0.12" stop-color="#f5f5f5"/>
      <stop offset="0.5" stop-color="#cfced2"/>
      <stop offset="1" stop-color="#99959a"/>
    </linearGradient>
    <linearGradient id="silver-side-right" gradientUnits="userSpaceOnUse" x1="999" y1="0" x2="1138" y2="0">
      <stop offset="0" stop-color="#9a979b"/>
      <stop offset="0.35" stop-color="#7f7c81"/>
      <stop offset="1" stop-color="#a8a6aa"/>
    </linearGradient>
    <linearGradient id="silver-glue" gradientUnits="userSpaceOnUse" x1="1138" y1="0" x2="1192" y2="0">
      <stop offset="0" stop-color="#b3b2b6"/>
      <stop offset="1" stop-color="#d6d6d7"/>
    </linearGradient>
  </defs>

  <!-- Top flaps -->
  <g class="top-flaps">
    <rect class="panel-black" x="106" y="30" width="373" height="233"/>
    <line class="fold" x1="106" y1="65" x2="479" y2="65"/>
    <line class="fold" x1="106" y1="164" x2="479" y2="164"/>
    <rect class="hang-slot" x="264" y="122" width="58" height="13" rx="6.5"/>
    <circle class="hang-slot" cx="292" cy="137" r="5"/>
    <rect class="hang-slot" x="264" y="193" width="58" height="13" rx="6.5"/>
    <circle class="hang-slot" cx="292" cy="191" r="5"/>

    <path class="panel-black" d="M481 263 L489 256 L489 155 L606 155 L621 263 Z"/>

    <rect class="panel-black" x="622" y="69" width="377" height="194"/>
    <line class="fold" x1="622" y1="123" x2="999" y2="123"/>

    <path class="panel-black" d="M999 263 L1014 155 L1131 155 L1131 256 L1138 263 Z"/>
  </g>

  <!-- Black header band -->
  <g class="header-band">
    <rect class="panel-black" x="104" y="263" width="1034" height="61"/>
    <path class="panel-black" d="M1138 263 L1192 270 L1192 324 L1138 324 Z"/>
  </g>

  <!-- Silver body panels -->
  <g class="body-panels">
    <rect x="104" y="344" width="377" height="351" fill="url(#silver-back)"/>
    <rect x="481" y="344" width="140" height="351" fill="url(#silver-side-left)"/>
    <rect x="621" y="344" width="378" height="351" fill="url(#silver-front)"/>
    <rect x="999" y="344" width="139" height="351" fill="url(#silver-side-right)"/>
    <path d="M1138 344 L1192 344 L1192 687 L1138 695 Z" fill="url(#silver-glue)"/>
    <rect class="window-cutout" x="880" y="344" width="258" height="193"/>
  </g>

  <!-- Yellow band -->
  <rect class="band-yellow" x="104" y="324" width="1088" height="20"/>

  <!-- Tuck tab on back panel -->
  <g class="back-tab">
    <rect x="248" y="695" width="89" height="53" fill="url(#silver-back)"/>
    <rect class="fold" x="248" y="605" width="89" height="90"/>
  </g>

  <!-- Bottom flaps -->
  <g class="bottom-flaps">
    <path d="M481 695 L489 703 L489 802 L606 802 L621 695 Z" fill="url(#silver-side-left)"/>
    <rect x="622" y="695" width="377" height="192" fill="url(#silver-front)"/>
    <line class="fold" x1="622" y1="833" x2="999" y2="833"/>
    <rect class="hang-slot" x="762" y="827" width="96" height="14" rx="7"/>
    <path d="M999 695 L1014 802 L1131 802 L1131 703 L1138 695 Z" fill="url(#silver-side-right)"/>
  </g>

  <!-- Fold lines -->
  <g class="folds">
    <line class="fold" x1="104" y1="263" x2="1192" y2="263"/>
    <line class="fold" x1="481" y1="263" x2="481" y2="695"/>
    <line class="fold" x1="621" y1="263" x2="621" y2="695"/>
    <line class="fold" x1="999" y1="263" x2="999" y2="695"/>
    <line class="fold" x1="1138" y1="263" x2="1138" y2="695"/>
    <line class="fold" x1="104" y1="695" x2="1138" y2="695"/>
  </g>
</svg>
</body>
</html>
```